Family Ranch with a hobby vineyard needs 2 wine labels for our first harvest

Design 2 wine labels (front and back) with the Morvasco Ranch logo.
Label 1:
Sauvignon Blanc
Alc. 12.5% by Vol.
Palos Verdes Peninsula - add as the region
Year 2022
Label 2:
Cabernet Sauvignon
Alc. 13.5% by Vol.
Year 2022
For the back label design:
GOVERNMENT WARNING: (1) According to the Surgeon General, women
should not drink alcoholic beverages during pregnancy because of the risk of
birth defects. (2) Consumption of alcoholic beverages impairs your ability to
drive a car or operate machinery, and may cause health problems.
Contains Sulfates.
750ML
I just received the bottles and have attached a picture.

```html
<!DOCTYPE html>
<html lang="en">
<head>
<meta charset="utf-8">
<title>Morvasco Ranch Wine Labels</title>
<link href="https://fonts.googleapis.com/css2?family=Montserrat:wght@400;500;600&family=Pinyon+Script&family=Roboto:wght@400;700&display=swap" rel="stylesheet">
<style>
  :root {
    --backdrop: #c9cacd;
    --label-paper: #fffff8;
    --ink: #111111;
    --gold: #b8923a;
    --gold-soft: #c9a55a;
    --pattern: #efeee8;
    --cab-accent: #fcd900;
    --sb-accent: #e43a25;
  }
  * { box-sizing: border-box; margin: 0; padding: 0; }
  html, body { width: 800px; height: 1200px; overflow: hidden; }
  body {
    background: var(--backdrop);
    position: relative;
    font-family: "Montserrat", sans-serif;
    color: var(--ink);
  }
  .front-label {
    position: absolute;
    top: 300px;
    width: 370px;
    height: 370px;
    text-align: center;
  }
  .front-label--cabernet { left: 20px; }
  .front-label--sauvignon { left: 410px; }
  .label-shape { position: absolute; inset: 0; width: 100%; height: 100%; }
  .label-pattern {
    position: absolute;
    right: 0;
    top: 110px;
    width: 190px;
    height: 200px;
    background: radial-gradient(circle at 60% 50%, var(--pattern), transparent 70%);
  }
  .label-content { position: relative; padding-top: 38px; }
  .brand-mark {
    width: 40px; height: 40px;
    margin: 0 auto 10px;
    border-radius: 50%;
    background: var(--gold);
  }
  .brand-name {
    font-weight: 600;
    font-size: 17px;
    letter-spacing: 2px;
    color: var(--gold);
    text-transform: uppercase;
  }
  .variety {
    margin-top: 26px;
    font-weight: 600;
    font-size: 25px;
    line-height: 28px;
    letter-spacing: 7px;
    text-transform: uppercase;
    padding-left: 7px;
  }
  .wine-style {
    margin-top: -20px;
    font-family: "Pinyon Script", cursive;
    font-size: 46px;
    line-height: 52px;
    color: var(--gold);
  }
  .region {
    margin-top: 20px;
    font-size: 10px;
    letter-spacing: 3px;
    text-transform: uppercase;
  }
  .vintage {
    margin-top: 12px;
    font-weight: 600;
    font-size: 12px;
    letter-spacing: 3px;
  }
  .alcohol {
    margin-top: 18px;
    font-size: 10px;
    letter-spacing: 0.5px;
  }
  .back-label {
    position: absolute;
    left: 215px;
    top: 710px;
    width: 370px;
    height: 160px;
    background: var(--label-paper);
    border-radius: 9px;
    padding: 22px 28px 0;
    font-family: "Roboto", sans-serif;
    font-size: 10.6px;
    line-height: 13.4px;
    text-align: center;
  }
  .warning { text-align: justify; text-align-last: center; }
  .warning strong { font-weight: 700; }
  .sulfites { margin-top: 14px; }
  .volume { margin-top: 13px; }
</style>
</head>
<body>

  <section class="front-label front-label--cabernet">
    <svg class="label-shape" viewBox="0 0 370 370" aria-hidden="true">
      <defs><clipPath id="cab-clip"><path d="M0 42 Q0 22 20 18 Q185 -16 350 18 Q370 22 370 42 V360 Q370 370 360 370 H10 Q0 370 0 360 Z"/></clipPath></defs>
      <path d="M0 42 Q0 22 20 18 Q185 -16 350 18 Q370 22 370 42 V360 Q370 370 360 370 H10 Q0 370 0 360 Z" fill="var(--label-paper)"/>
      <ellipse cx="185" cy="392" rx="66" ry="30" fill="var(--cab-accent)" clip-path="url(#cab-clip)"/>
    </svg>
    <div class="label-pattern" role="img" aria-label="Faint fingerprint texture"></div>
    <div class="label-content">
      <div class="brand-mark"></div>
      <p class="brand-name">Morvasco Ranch</p>
      <h2 class="variety">Cabernet<br>Sauvignon</h2>
      <p class="wine-style">Red Wine</p>
      <p class="region">Palos Verdes Peninsula</p>
      <p class="vintage">2022</p>
      <p class="alcohol">ALC. 13.5% / VOL.</p>
    </div>
  </section>

  <section class="front-label front-label--sauvignon">
    <svg class="label-shape" viewBox="0 0 370 370" aria-hidden="true">
      <defs><clipPath id="sb-clip"><path d="M0 42 Q0 22 20 18 Q185 -16 350 18 Q370 22 370 42 V360 Q370 370 360 370 H10 Q0 370 0 360 Z"/></clipPath></defs>
      <path d="M0 42 Q0 22 20 18 Q185 -16 350 18 Q370 22 370 42 V360 Q370 370 360 370 H10 Q0 370 0 360 Z" fill="var(--label-paper)"/>
      <ellipse cx="185" cy="392" rx="66" ry="30" fill="var(--sb-accent)" clip-path="url(#sb-clip)"/>
    </svg>
    <div class="label-pattern" role="img" aria-label="Faint fingerprint texture"></div>
    <div class="label-content">
      <div class="brand-mark"></div>
      <p class="brand-name">Morvasco Ranch</p>
      <h2 class="variety">Sauvignon<br>Blanc</h2>
      <p class="wine-style">Red Wine</p>
      <p class="region">Palos Verdes Peninsula</p>
      <p class="vintage">2022</p>
      <p class="alcohol">ALC. 12.5% / VOL.</p>
    </div>
  </section>

  <section class="back-label">
    <p class="warning"><strong>GOVERNMENT WARNING:</strong> (1) According to the Surgeon General, women should not drink alcoholic beverages during pregnancy because of the risk of birth defects. (2) Consumption of alcoholic beverages impairs your ability to drive a car or operate machinery, and may cause health problems.</p>
    <p class="sulfites">Contains Sulfates</p>
    <p class="volume">750ML</p>
  </section>

</body>
</html>
```